Dolsemk Business Cards

Business cards for real estate
Target Market(s)
Real estate
Industry/Entity Type
Real Estate Agent
Font styles to use
Serif
Requirements
Must have
- Photo and logo

```html
<!DOCTYPE html>
<html lang="en">
<head>
<meta charset="utf-8">
<title>Dolsemk Realty Business Cards</title>
<link rel="stylesheet" href="https://fonts.googleapis.com/css2?family=Cinzel:wght@400;600&family=Tinos&display=swap">
<style>
  :root {
    --backdrop: #ebe6de;
    --maroon: #8a2230;
    --maroon-deep: #6e1824;
    --bronze: #b46a45;
    --gold: #c9a56a;
    --gold-light: #ecd6a8;
    --ink: #1f1a1a;
    --white: #ffffff;
    --black: #151515;
  }
  * { margin: 0; padding: 0; box-sizing: border-box; }
  html, body { width: 900px; height: 1200px; overflow: hidden; }
  body { background: var(--backdrop); position: relative; font-family: "Tinos", "Times New Roman", serif; }

  .card {
    position: absolute; left: 85px; width: 735px; height: 430px;
    border-radius: 18px; overflow: hidden;
    box-shadow: 0 6px 14px rgba(0,0,0,0.25);
  }
  .card-front { top: 138px; background: radial-gradient(ellipse at 45% 70%, var(--bronze) 0%, var(--maroon) 55%, var(--maroon-deep) 100%); }
  .card-back { top: 633px; background: var(--white); }

  /* front */
  .front-header {
    position: absolute; left: 0; top: 0; width: 100%; height: 208px;
    background: linear-gradient(90deg, #ffffff 0%, #f6f3f1 55%, #d9a277 80%, #a85f3c 100%);
  }
  .gold-rule { position: absolute; left: 0; width: 100%; height: 5px;
    background: linear-gradient(90deg, var(--gold) 0%, var(--gold-light) 50%, var(--gold) 100%); }
  .gold-rule.upper { top: 210px; }
  .gold-rule.lower { top: 410px; }

  .brand { position: absolute; display: flex; align-items: center; gap: 24px; }
  .brand-dot { width: 130px; height: 130px; border-radius: 50%; background: var(--maroon); flex: none; }
  .brand-name {
    font-family: "Cinzel", "Times New Roman", serif; font-weight: 400; color: var(--ink);
    line-height: 1.05; letter-spacing: 2px;
  }
  .brand-name span { display: block; }
  .front-brand { left: 42px; top: 48px; }
  .front-brand .brand-name { font-size: 46px; }
  .front-brand .brand-name span + span { letter-spacing: 7px; }

  .agent-photo {
    position: absolute; left: 445px; top: 20px; width: 255px; height: 300px;
    background: linear-gradient(180deg, #c79b7e 0%, #2a2c36 45%, #1b1d26 100%);
    border-radius: 120px 120px 6px 6px;
  }
  .agent-name {
    position: absolute; left: 420px; width: 300px; top: 338px; text-align: center;
    font-family: "Cinzel", "Times New Roman", serif; font-size: 21px; color: var(--white); letter-spacing: 0.5px;
  }
  .agent-title {
    position: absolute; left: 420px; width: 300px; top: 366px; text-align: center;
    font-size: 17px; color: var(--gold);
  }

  .contact-list { position: absolute; left: 38px; top: 258px; list-style: none; }
  .contact-list li { display: flex; align-items: center; gap: 9px; height: 26.5px; color: var(--white); font-size: 15.5px; }
  .contact-list svg { width: 17px; height: 17px; fill: var(--gold); flex: none; }

  /* back */
  .house-photo {
    position: absolute; inset: 0;
    background: linear-gradient(180deg, #e9ecf1 0%, #eef0ee 45%, #dfe6d9 68%, #d5dfcc 100%);
  }
  .back-brand { left: 70px; top: 68px; }
  .back-brand .brand-name { font-size: 46px; }
  .back-brand .brand-name span + span { letter-spacing: 7px; }
  .swooshes { position: absolute; left: 0; top: 0; }
  .back-web {
    position: absolute; left: 68px; top: 383px; color: var(--white);
    font-size: 16px; letter-spacing: 2.5px;
  }
  .cert-badges { position: absolute; right: 36px; top: 370px; display: flex; gap: 16px; }
  .cert-badge { width: 26px; height: 30px; background: var(--white); border-radius: 2px; }
</style>
</head>
<body>

  <section class="card card-front">
    <div class="front-header"></div>
    <div class="gold-rule upper"></div>
    <div class="gold-rule lower"></div>

    <div class="brand front-brand">
      <div class="brand-dot"></div>
      <div class="brand-name"><span>DOLSEMK</span><span>REALTY</span></div>
    </div>

    <div class="agent-photo" role="img" aria-label="Portrait photo of the agent in a dark suit"></div>
    <div class="agent-name">YOUR NAME HERE</div>
    <div class="agent-title">Estate Agent</div>

    <ul class="contact-list">
      <li><svg viewBox="0 0 16 16"><path d="M4 1h8a1 1 0 0 1 1 1v12a1 1 0 0 1-1 1H4a1 1 0 0 1-1-1V2a1 1 0 0 1 1-1zm1 2v9h6V3z"/></svg>0712-4480-2916</li>
      <li><svg viewBox="0 0 16 16"><path d="M3 1l3 3-1.5 2a9 9 0 0 0 5.5 5.5L12 10l3 3-2 2C7 15 1 9 1 3z"/></svg>0938-5571-6024</li>
      <li><svg viewBox="0 0 16 16"><path d="M1 3h14v10H1zm1 1.2V5l6 4 6-4v-.8L8 8z"/></svg>info@dolsemkrealty.com</li>
      <li><svg viewBox="0 0 16 16"><path d="M8 1a7 7 0 1 0 0 14A7 7 0 0 0 8 1zm0 1.5c.9 1 1.5 2.5 1.7 4H6.3C6.5 5 7.1 3.5 8 2.5zM6.3 8h3.4c-.2 1.5-.8 3-1.7 4-.9-1-1.5-2.5-1.7-4zM2.6 8h2.2c.1 1.4.5 2.7 1.1 3.8A5.5 5.5 0 0 1 2.6 8zm0-1.5a5.5 5.5 0 0 1 3.3-4.3c-.6 1.1-1 2.4-1.1 4.3zm8.6 0c-.1-1.9-.5-3.2-1.1-4.3a5.5 5.5 0 0 1 3.3 4.3zm0 1.5h2.2a5.5 5.5 0 0 1-3.3 3.8c.6-1.1 1-2.4 1.1-3.8z"/></svg>www.dolsemkrealty.com</li>
      <li><svg viewBox="0 0 16 16"><path d="M8 1a5 5 0 0 0-5 5c0 4 5 9 5 9s5-5 5-9a5 5 0 0 0-5-5zm0 3a2 2 0 1 1 0 4 2 2 0 0 1 0-4z"/></svg>2417 Alderbrook Road, Suite 4, Fenwick, MD 20944</li>
    </ul>
  </section>

  <section class="card card-back">
    <div class="house-photo" role="img" aria-label="Faded photo of a suburban house with a green lawn"></div>

    <div class="brand back-brand">
      <div class="brand-dot"></div>
      <div class="brand-name"><span>DOLSEMK</span><span>REALTY</span></div>
    </div>

    <svg class="swooshes" width="735" height="430" viewBox="0 0 735 430" aria-hidden="true">
      <defs>
        <linearGradient id="maroon-sweep" x1="0" y1="0" x2="1" y2="0">
          <stop offset="0" stop-color="#8a2230"/>
          <stop offset="0.7" stop-color="#b0603f"/>
          <stop offset="1" stop-color="#8a2230"/>
        </linearGradient>
      </defs>
      <path d="M0 352 C260 340 480 300 640 170 C560 290 500 370 440 430 L0 430 Z" fill="url(#maroon-sweep)"/>
      <path d="M735 135 C630 215 530 320 455 430 L735 430 Z" fill="#151515"/>
      <path d="M0 336 C300 326 540 250 735 140" fill="none" stroke="#ffffff" stroke-width="6"/>
      <path d="M0 326 C300 314 540 236 735 126" fill="none" stroke="#151515" stroke-width="14"/>
      <path d="M735 35 C650 90 570 250 430 430" fill="none" stroke="#8a2230" stroke-width="10"/>
      <path d="M735 110 C640 170 540 300 470 430" fill="none" stroke="#ffffff" stroke-width="7"/>
      <path d="M735 70 C640 130 560 280 455 430" fill="none" stroke="#8a2230" stroke-width="6"/>
    </svg>

    <div class="back-web">WWW.DOLSEMKREALTY.COM</div>
    <div class="cert-badges">
      <div class="cert-badge"></div>
      <div class="cert-badge"></div>
    </div>
  </section>

</body>
</html>
```